Business Cards that are elegant and wow

I want to create and print business cards that represent my brand and stand out from the rest. We want to ensure they stay in our branding and the integrity is not lost. I am happy to look at different shapes like square etc.

It will be printed on very thick cards and will be stylish .

I want to create and print business cards that represent my brand and stand out from the rest. We want to ensure they stay in ur branding and the integrity is not lost. I am happy to look at different shapes like square etc.

Target Market(s)

real estate professionals

Industry/Entity Type

Real Estate

Contact Information for Business Card

Maren Holt
hello@brightfernrealty.com.au
brightfernrealty.com.au
0487 316 252 (SMS)

Colors

Designer to choose colors to be used in the design.

Requirements
Must have
• My logo
• email
• website
• Name
Nice to have
• I like the idea of printing with foil or spot gloss. You want it to stand out in a sea.
Should not have
• I would like you to stay in my colour themes. Don't change the colour of my logo

```html
<!DOCTYPE html>
<html lang="en">
<head>
<meta charset="utf-8">
<title>Bright Fern Realty – Business Card</title>
<link href="https://fonts.googleapis.com/css2?family=Montserrat:wght@600;800&family=Oswald:wght@300;400&display=swap" rel="stylesheet">
<style>
  :root {
    --page: #ece6df;
    --sky: #00b2f0;
    --lilac: #9a86c0;
    --rose: #ec3f8e;
    --magenta: #e8177a;
    --mist: #e4e4ea;
    --paper: #ffffff;
    --ink-light: #ffffff;
  }
  * { margin: 0; padding: 0; box-sizing: border-box; }
  html, body {
    width: 1200px; height: 1200px; overflow: hidden;
    background: var(--page);
  }
  .sheet { position: relative; width: 1200px; height: 1200px; }
  .card {
    position: absolute; left: 160px;
    width: 880px; height: 500px;
    border-radius: 6px; overflow: hidden;
    box-shadow: 0 10px 30px rgba(80, 60, 50, 0.18);
  }
  .card-front {
    top: 70px;
    background: linear-gradient(150deg, var(--sky) 0%, #4a9bd6 28%, var(--lilac) 55%, #c873ae 78%, var(--rose) 100%);
  }
  .card-back { top: 630px; }

  .brand {
    position: absolute; display: flex; align-items: center; gap: 22px;
    white-space: nowrap;
  }
  .brand-dot { flex: none; border-radius: 50%; border-style: solid; }
  .brand-name {
    font-family: "Montserrat", sans-serif; font-weight: 600;
    letter-spacing: 0.04em; text-transform: uppercase; line-height: 1;
    white-space: nowrap;
  }
  .card-front .brand { left: 50%; top: 50%; transform: translate(-50%, -50%); }
  .card-front .brand-dot {
    width: 92px; height: 92px; border-width: 5px; border-color: var(--ink-light);
  }
  .card-front .brand-name { font-size: 40px; color: var(--ink-light); }

  .back-art { position: absolute; inset: 0; width: 100%; height: 100%; }
  .card-back .brand { left: 56px; top: 140px; gap: 12px; }
  .card-back .brand-dot {
    width: 44px; height: 44px; border-width: 4px; border-color: var(--sky);
  }
  .card-back .brand-name { font-size: 20px; color: var(--sky); }

  .contact {
    position: absolute; right: 48px; top: 66px;
    text-align: right; color: var(--ink-light);
  }
  .contact-name {
    font-family: "Montserrat", sans-serif; font-weight: 800;
    font-size: 34px; letter-spacing: 0.04em; text-transform: uppercase;
    white-space: nowrap; line-height: 1.1;
  }
  .contact-line {
    font-family: "Oswald", sans-serif; font-weight: 300;
    font-size: 22px; line-height: 1.35; white-space: nowrap;
    display: flex; justify-content: flex-end; align-items: center; gap: 10px;
  }
  .contact-phone { margin-top: 8px; font-size: 22px; }
  .contact-details {
    position: absolute; right: 48px; bottom: 46px;
    text-align: right; color: var(--ink-light);
  }
  .contact-company { font-size: 19px; padding-right: 32px; }
  .icon { width: 22px; height: 22px; flex: none; }
</style>
</head>
<body>
<main class="sheet">

  <section class="card card-front" aria-label="Card front">
    <div class="brand">
      <span class="brand-dot"></span>
      <span class="brand-name">Bright Fern Realty</span>
    </div>
  </section>

  <section class="card card-back" aria-label="Card back">
    <svg class="back-art" viewBox="0 0 880 500" preserveAspectRatio="none" aria-hidden="true">
      <defs>
        <linearGradient id="backFill" x1="0.35" y1="0" x2="0.75" y2="1">
          <stop offset="0" stop-color="#00a6e6"/>
          <stop offset="0.4" stop-color="#8a88bf"/>
          <stop offset="0.7" stop-color="#c069a3"/>
          <stop offset="1" stop-color="#ec3f8e"/>
        </linearGradient>
      </defs>
      <rect width="880" height="500" fill="url(#backFill)"/>
      <path d="M0 0 H515 C515 250 390 470 190 500 H0 Z" fill="var(--magenta)"/>
      <path d="M0 0 H495 C490 240 370 440 180 478 L0 486 Z" fill="var(--mist)"/>
      <path d="M0 0 H470 C463 230 345 425 160 462 L0 470 Z" fill="var(--paper)"/>
    </svg>

    <div class="brand">
      <span class="brand-dot"></span>
      <span class="brand-name">Bright Fern Realty</span>
    </div>

    <div class="contact">
      <p class="contact-name">Maren Holt</p>
      <p class="contact-line contact-phone">0487 316 252
        <svg class="icon" viewBox="0 0 24 24" aria-hidden="true"><rect x="7" y="2" width="10" height="20" rx="2" fill="none" stroke="#fff" stroke-width="1.8"/><line x1="10" y1="18" x2="14" y2="18" stroke="#fff" stroke-width="1.8"/></svg>
      </p>
    </div>

    <div class="contact-details">
      <p class="contact-line contact-company">Bright Fern Realty Pvt.Ltd</p>
      <p class="contact-line">brightfernrealty.com.au
        <svg class="icon" viewBox="0 0 24 24" aria-hidden="true"><g fill="none" stroke="#fff" stroke-width="1.6"><circle cx="12" cy="12" r="9"/><ellipse cx="12" cy="12" rx="4" ry="9"/><line x1="3" y1="12" x2="21" y2="12"/></g></svg>
      </p>
      <p class="contact-line">hello@brightfernrealty.com.au
        <svg class="icon" viewBox="0 0 24 24" aria-hidden="true"><rect x="2" y="5" width="20" height="14" fill="#fff"/><path d="M2 5 L12 13 L22 5" fill="none" stroke="#c069a3" stroke-width="1.4"/></svg>
      </p>
    </div>
  </section>

</main>
</body>
</html>
```